One-page magazine ad for accountant serving the non-profit industry

I am Certified Public Accountant placing a one-page ad in Harvestlight Journal. The ad will be seen by churches and other non-profit organizations.
Harvestlight Journal requires the following:
Accepted file formats:
a) Press ready PDF with all fonts embedded. OR
b) Flattened CMYK Abode Photoshop PSD or illustrator PDF or EPS with all fonts outlined.
Ad Specs:
Trim 8" x 10.5"
Live 7.5" x 10"
Bleed 8.25" x 10.75"

I would like the ad to state the following information:

Marcus T. Velloway, CPA, CGMA

I am Certified Public Accountant with over 30 years of experience serving the accounting and tax needs of churches and non-profit organizations.

Some of the services I can offer:

Audits, Reviews, Compilations
Bookkeeping Services
Payroll Taxes
501C3 - IRS exemption applications
Clergy Housing Allowance issues and Personal Taxes

```html
<!DOCTYPE html>
<html lang="en">
<head>
<meta charset="utf-8">
<title>Marcus T. Velloway, CPA, CGMA – Magazine Ad</title>
<link rel="stylesheet" href="https://fonts.googleapis.com/css2?family=Cinzel:wght@400;500;600&family=Arial&display=swap">
<style>
  :root {
    --page-bg: #ffffff;
    --guide-line: #c9c9c9;
    --guide-label: #222222;
    --header-black: #000000;
    --band-maroon: #955252;
    --panel-white: #ffffff;
    --intro-brown: #5b3d2c;
    --heading-red: #9b3a3a;
    --service-ink: #333333;
    --footer-blue: #4a86b0;
    --footer-ink: #ffffff;
    --photo-light: #eef3f8;
    --photo-mid: #b9cde0;
    --photo-dark: #6f8aa5;
  }
  * { box-sizing: border-box; margin: 0; padding: 0; }
  html, body { width: 929px; height: 1200px; overflow: hidden; background: var(--page-bg); }
  .canvas { position: relative; width: 929px; height: 1200px; font-family: "Cinzel", serif; }

  .guide { position: absolute; border: 1.5px solid var(--guide-line); }
  .guide--bleed { left: 15px; top: 15px; width: 899px; height: 1168px; }
  .guide--trim { left: 30px; top: 30px; width: 869px; height: 1137px; }
  .guide-label {
    position: absolute; font-family: Arial, Helvetica, sans-serif; font-size: 11px;
    color: var(--guide-label); background: var(--page-bg); padding: 0 3px; line-height: 1;
  }
  .guide-label--bleed { left: 24px; top: 9px; }
  .guide-label--trim { left: 180px; top: 24px; }
  .guide-label--live { left: 66px; top: 62px; color: #ffffff; background: none; }

  .ad { position: absolute; left: 56px; top: 53px; width: 817px; height: 1089px; }

  .ad-header {
    position: absolute; left: 0; top: 0; width: 817px; height: 166px;
    background: var(--header-black); display: flex; align-items: center; justify-content: center;
  }
  .ad-header__name {
    color: #ffffff; font-weight: 500; font-size: 38px; letter-spacing: 0.5px; margin-top: 12px;
  }

  .ad-band { position: absolute; left: 0; top: 166px; width: 817px; height: 462px; background: var(--band-maroon); }
  .ad-panel {
    position: absolute; left: 150px; top: 0; width: 517px; height: 462px;
    background: var(--panel-white); text-align: center;
  }
  .ad-intro {
    position: absolute; left: 0; top: 45px; width: 100%;
    color: var(--intro-brown); font-size: 20px; line-height: 32.5px; letter-spacing: 1.2px;
  }
  .ad-services__heading {
    position: absolute; left: 0; top: 210px; width: 100%;
    color: var(--heading-red); font-size: 20px; letter-spacing: 1px;
  }
  .ad-services__list {
    position: absolute; left: 0; top: 256px; width: 100%; list-style: none;
    color: var(--service-ink); font-size: 16.5px; letter-spacing: 0.6px;
  }
  .ad-services__list li { line-height: 33px; }
  .ad-services__list li.wrap { line-height: 27px; margin-top: 3px; }

  .ad-photo {
    position: absolute; left: 0; top: 628px; width: 817px; height: 355px;
    background: linear-gradient(120deg, var(--photo-light) 0%, var(--photo-mid) 45%, var(--photo-light) 70%, var(--photo-dark) 100%);
  }

  .ad-footer {
    position: absolute; left: 0; top: 983px; width: 817px; height: 106px;
    background: var(--footer-blue); color: var(--footer-ink); text-align: center;
    letter-spacing: 3px; font-size: 15px;
  }
  .ad-footer__address { position: absolute; left: 0; top: 22px; width: 100%; }
  .ad-footer__contacts { position: absolute; left: 0; top: 54px; width: 100%; word-spacing: 6px; }
  .ad-footer__contacts span { margin: 0 10px; }
</style>
</head>
<body>
<div class="canvas">
  <div class="guide guide--bleed"></div>
  <div class="guide guide--trim"></div>
  <span class="guide-label guide-label--bleed">Bleed 8.25" x 10.75"</span>
  <span class="guide-label guide-label--trim">Trim 8" x 10.5"</span>

  <main class="ad">
    <header class="ad-header">
      <h1 class="ad-header__name">Marcus T. Velloway, CPA, CGMA</h1>
    </header>

    <section class="ad-band">
      <div class="ad-panel">
        <p class="ad-intro">I am Certified Public Accountant<br>with over 30 years of experience serving<br>the accounting and tax needs of<br>churches and non-profit organizations.</p>
        <h2 class="ad-services__heading">Some of the services I can offer:</h2>
        <ul class="ad-services__list">
          <li>Audits, Reviews, Compilations</li>
          <li>Bookkeeping Services</li>
          <li>Payroll Taxes</li>
          <li>501C3 - IRS exemption applications</li>
          <li class="wrap">Clergy Housing Allowance issues<br>and Personal Taxes</li>
        </ul>
      </div>
    </section>

    <div class="ad-photo" role="img" aria-label="Photo of hands working with calculators, pens and financial charts on a desk, with a rising bar chart overlay"></div>

    <footer class="ad-footer">
      <p class="ad-footer__address">Address:</p>
      <p class="ad-footer__contacts"><span>Telephone: 000-0000</span><span>Fax: 000-0000</span><span>Email:</span><span>Mobile:</span></p>
    </footer>
  </main>
  <span class="guide-label guide-label--live">Live 7.5" x 10"</span>
</div>
</body>
</html>
```